Online Travel Agency card design with 2 logos

Need a two sided business card design for online tourism agency which is based in Istanbul Turkey.
Need a business card design where it shows the travel agency logo but also the logo and information of the parent company as well.Parent company logo is just text with 2 different colors. (Arial font with text ToreVextra "Tore"- hex #172841 and "Vextra" hex-#FF7F00)
Both logos are uploaded.
Target Market(s)
travel , online
Industry/Entity Type
Travel
Contact Information for Business Card
The information on the card should be as :
Travel Agency Logo logo (pnlogo)
Parent Company logo(torelogo)
Company information :ToreVextra Turizm ve Bilgi Teknolojileri A.Ş
Address of company
Tel
Email
Name
Position(english and turkish)

```html
<!DOCTYPE html>
<html lang="tr">
<head>
<meta charset="utf-8">
<title>ToreVextra – pernavia business card</title>
<link rel="stylesheet" href="https://fonts.googleapis.com/css2?family=Open+Sans:wght@400;700;800&family=Montserrat:wght@500&family=Courier+Prime:wght@400;700&display=swap">
<style>
  :root {
    --navy: #172841;
    --sky: #6fcfe8;
    --sky-pale: #e4f5fb;
    --sky-mid: #bfe8f3;
    --white: #ffffff;
    --ink: #1d1d1f;
    --page: #ffffff;
  }
  * { margin: 0; padding: 0; box-sizing: border-box; }
  html, body {
    width: 1200px; height: 1200px; overflow: hidden;
    background: var(--page);
  }
  .canvas { position: relative; width: 1200px; height: 1200px; }

  .card {
    position: absolute; left: 210px; width: 768px;
    overflow: hidden;
    box-shadow: 10px 12px 14px rgba(0,0,0,0.22);
  }
  .card--front {
    top: 77px; height: 434px;
    background: linear-gradient(90deg, var(--sky-pale) 0%, var(--sky-mid) 75%, var(--sky) 100%);
  }
  .card--back { top: 620px; height: 426px; background: var(--sky); }

  .card__shapes { position: absolute; inset: 0; width: 100%; height: 100%; }

  .legal-name {
    position: absolute; left: 0; width: 700px; bottom: 0; height: 48px;
    display: flex; align-items: center; justify-content: center;
    font-family: "Montserrat", sans-serif; font-weight: 500;
    font-size: 20px; color: var(--white); white-space: nowrap;
  }

  .parent-name {
    position: absolute;
    font-family: "Open Sans", sans-serif; font-weight: 400;
    color: var(--navy); letter-spacing: -0.5px; white-space: nowrap;
    line-height: 1;
  }
  .agency-name {
    position: absolute;
    font-family: "Open Sans", sans-serif; font-weight: 700;
    color: var(--navy); white-space: nowrap; line-height: 1;
  }

  .card--front .parent-name { left: 27px; top: 18px; font-size: 35px; }
  .card--front .agency-name { left: 262px; top: 14px; font-size: 40px; }

  .brand-disc {
    position: absolute; left: 196px; top: 99px;
    width: 188px; height: 188px; border-radius: 50%;
    background: var(--navy);
  }

  .card--back .parent-name { right: 14px; top: 42px; font-size: 32px; }
  .card--back .agency-name { right: 14px; top: 92px; font-size: 36px; }

  .person { position: absolute; left: 68px; top: 54px; }
  .person__name {
    font-family: "Open Sans", sans-serif; font-size: 46px; line-height: 1;
    color: var(--navy); letter-spacing: 0.5px; font-weight: 400;
  }
  .person__first { font-weight: 800; }
  .person__role {
    font-family: "Courier Prime", monospace; font-weight: 700; font-size: 13px;
    letter-spacing: 5.6px; line-height: 18px;
  }
  .person__role--en { color: var(--navy); margin-top: 8px; }
  .person__role--tr { color: var(--white); margin-top: 2px; }

  .contact { position: absolute; left: 67px; top: 163px; list-style: none; }
  .contact__item {
    display: flex; align-items: center; gap: 11px;
    font-family: "Open Sans", sans-serif; font-weight: 700;
    font-size: 12.5px; line-height: 19px; color: var(--ink);
    margin-bottom: 20px;
  }
  .contact__icon { width: 36px; height: 36px; flex: none; }
</style>
</head>
<body>
<main class="canvas">

  <section class="card card--front" aria-label="Card front">
    <svg class="card__shapes" viewBox="0 0 768 434" aria-hidden="true">
      <defs>
        <linearGradient id="fold-light" x1="0" y1="1" x2="1" y2="0">
          <stop offset="0" stop-color="#6fcfe8"/>
          <stop offset="1" stop-color="#e6f6fb"/>
        </linearGradient>
        <linearGradient id="fold-dark" x1="0" y1="0" x2="1" y2="0.3">
          <stop offset="0" stop-color="#6a9ab0"/>
          <stop offset="0.55" stop-color="#2b4560"/>
          <stop offset="1" stop-color="#172841"/>
        </linearGradient>
      </defs>
      <rect x="0" y="386" width="768" height="48" fill="#172841"/>
      <path d="M666 0 L768 0 L768 419 L478 228 Q460 217 478 204 Z" fill="#6dcfe8"/>
      <path d="M714 0 L768 0 L768 415 L570 217 Z" fill="url(#fold-light)"/>
      <path d="M570 217 L768 415 L768 434 L672 434 L560 318 Q530 282 570 217 Z" fill="url(#fold-dark)"/>
    </svg>

    <div class="parent-name">ToreVextra</div>
    <div class="agency-name">pernavia</div>
    <div class="brand-disc" role="img" aria-label="pernavia brand mark"></div>
    <div class="legal-name">ToreVextra Turizm ve Bilgi Teknolojileri A.Ş</div>
  </section>

  <section class="card card--back" aria-label="Card back">
    <svg class="card__shapes" viewBox="0 0 768 426" aria-hidden="true">
      <path d="M576 0 L768 0 L768 412 L732 377 L494 112 Q480 100 494 86 Z" fill="#ffffff"/>
      <path d="M0 377 L732 377 L768 412 L768 426 L0 426 Z" fill="#172841"/>
    </svg>

    <div class="parent-name">ToreVextra</div>
    <div class="agency-name">pernavia</div>

    <div class="person">
      <h1 class="person__name"><span class="person__first">ARDA</span>KENTER</h1>
      <p class="person__role person__role--en">MARKETING DIRECTOR</p>
      <p class="person__role person__role--tr">PAZARLAMA DİREKTÖRÜ</p>
    </div>

    <ul class="contact">
      <li class="contact__item">
        <svg class="contact__icon" viewBox="0 0 36 36" aria-hidden="true">
          <circle cx="18" cy="18" r="16" fill="none" stroke="#fff" stroke-width="2"/>
          <path d="M10 18 L18 11 L26 18 L24 18 L24 25 L20 25 L20 20 L16 20 L16 25 L12 25 L12 18 Z" fill="#fff"/>
        </svg>
        <span>YOUR CITY ADDRESS<br>STREET LOCATION, NY CITY, USA</span>
      </li>
      <li class="contact__item">
        <svg class="contact__icon" viewBox="0 0 36 36" aria-hidden="true">
          <circle cx="18" cy="18" r="16" fill="none" stroke="#fff" stroke-width="2"/>
          <path d="M13 10 Q11 11 11 14 Q12 21 18 25 Q21 27 24 26 Q26 25 25.5 23.5 L23 21 Q22 20.5 21 21.5 L20 22.5 Q17 21 14.5 17 L15.5 16 Q16.5 15 16 14 L14.5 10.5 Q14 9.8 13 10 Z" fill="#fff"/>
        </svg>
        <span>+00 1234 5678 9012<br>+00 1234 5678 9012</span>
      </li>
      <li class="contact__item">
        <svg class="contact__icon" viewBox="0 0 36 36" aria-hidden="true">
          <circle cx="18" cy="18" r="16" fill="none" stroke="#fff" stroke-width="2"/>
          <rect x="10" y="12.5" width="16" height="11" fill="#fff"/>
          <path d="M10 12.5 L18 19 L26 12.5" fill="none" stroke="#6fcfe8" stroke-width="1.4"/>
        </svg>
        <span>INFO@TOREVEXTRA.COM</span>
      </li>
    </ul>

    <div class="legal-name">ToreVextra Turizm ve Bilgi Teknolojileri A.Ş</div>
  </section>

</main>
</body>
</html>
```